Web Design Project

Goal
Combine 2 sites into 1 and enhance functionality

Concept & Overview

My current websites are rowanvoices dot com and tidewaterguides dot org. They are not very popular but I run ads and capture leads and do a tidy bit, but I am going on tour and need to have my website upgrade.

My goal is to redesign rowanvoices and have it as a 10 page site that introduces me and also capture leads in an effective manner then introduce a 5 page system.

I need to update the layout and feel of the site to match the color and image of the book. Currently the book is at tidewaterguides.org and my speaking is at rowanvoices.com. I need the two to combine but I also need functionality to improve. I introduce a 5 step system and I think a visual image like this one can better introduce it.

Here: https://www.brightleafmedia.com/packages/kgt-marla-quinns-life-improvement-program.html

Then in there I need the Lesson Area

Like:

https://www.brightleafmedia.com/packages/kgt-marla-quinns-life-improvement-program.html

They are few samples I can show but this is the main concept.

Target Market(s)

Schools, colleges, churches, and youth organizations

Industry/Entity Type

Tour

Requirements
Must have
• A clean wide home page that is properly designed can do the job of leading to the optin without the sales look.

Nice to have
• https://www.brightleafmedia.com/packages/kgt-marla-quinns-life-improvement-program.html
Should not have
• Sales look and feel

```html
<!DOCTYPE html>
<html lang="en">
<head>
<meta charset="utf-8">
<title>Rowan Ellery</title>
<link href="https://fonts.googleapis.com/css2?family=Oswald:wght@300;400;500&family=Arimo:wght@400;700&display=swap" rel="stylesheet">
<style>
:root{
  --sky:#29a8ec;
  --sky-deep:#1690d8;
  --sky-soft:#bfe3f7;
  --navy:#14314a;
  --ink:#333;
  --muted:#666;
  --orange:#f7931e;
  --green:#8cc63f;
  --green-dark:#6aa82a;
  --panel:#f4f4f4;
  --line:#e2e2e2;
}
*{margin:0;padding:0;box-sizing:border-box}
html,body{width:711px;height:1200px;overflow:hidden;background:#fff;font-family:"Arimo",Arial,sans-serif;color:var(--ink)}
.page{position:relative;width:711px;height:1200px}
.abs{position:absolute}
.site-header{left:0;top:0;width:711px;height:49px;background:var(--sky)}
.site-name{left:123px;top:9px;font-family:"Oswald",sans-serif;font-size:24px;color:#fff;letter-spacing:.5px;font-weight:400}
.nav{left:0;top:49px;width:711px;height:31px;background:#f7f7f7;border-bottom:1px solid var(--line)}
.nav a{position:absolute;top:10px;font-size:7.5px;color:#444;text-decoration:none;font-weight:700;text-transform:uppercase}
.nav .active{left:123px;top:5px;width:80px;height:22px;background:var(--orange);color:#fff;text-align:center;line-height:22px}
.nav .active:after{content:"";position:absolute;left:35px;bottom:-5px;border:5px solid transparent;border-bottom:0;border-top-color:var(--orange)}
.hero{left:0;top:80px;width:711px;height:149px;background:linear-gradient(180deg,#8fd0f3,#d9f0fb 60%,#a8dbf5)}
.hero-box{left:123px;top:11px;width:464px;height:132px;background:var(--sky-deep)}
.portrait{left:6px;top:6px;width:80px;height:76px;background:linear-gradient(160deg,#7a6a5c,#2c2520)}
.hero-name{left:6px;top:86px;font-family:"Oswald",sans-serif;color:#fff;font-size:11px}
.hero-roles{left:6px;top:102px;list-style:none;color:#fff;font-size:6.5px;font-weight:700;line-height:8px}
.hero-roles li:before{content:"➜ "}
.hero-quote{left:96px;top:6px;width:360px;font-family:"Oswald",sans-serif;font-size:11px;line-height:15px;color:#fff}
.hero-text{left:96px;width:360px;font-size:6.4px;line-height:8.2px;color:#e8f5fd}
.read-more{left:96px;top:107px;width:48px;height:12px;border-radius:6px;background:#fff;color:var(--sky-deep);font-size:6.5px;font-weight:700;line-height:12px;padding-left:6px}
.section-title{font-family:"Oswald",sans-serif;font-size:10px;color:#222;font-weight:400}
.video{left:123px;top:259px;width:320px;height:179px;background:#111}
.video-frame{left:0;top:0;width:320px;height:158px;background:linear-gradient(135deg,#4a4e45,#2a2c2a 45%,#1b1d21)}
.video-icon{left:296px;width:18px;height:14px;border:1px solid #888;background:#222}
.video-bar{left:0;top:158px;width:320px;height:21px;background:#1c1c1c}
.optin{left:451px;top:259px;width:137px;height:146px;background:var(--panel)}
.optin-head{left:0;top:0;width:137px;height:26px;background:var(--navy);color:#fff;font-size:6.2px;font-weight:700;padding:5px 6px;line-height:8px}
.optin label{position:absolute;left:7px;font-size:6.2px;font-weight:700;color:#333}
.optin .field{position:absolute;left:7px;width:123px;height:10px;background:#fff;border:1px solid #ccc}
.optin-btn{left:7px;top:90px;width:123px;height:20px;border-radius:10px;background:var(--orange);color:#fff;font-size:9px;font-weight:700;text-align:center;line-height:20px}
.optin-foot{left:0;top:128px;width:137px;height:18px;background:var(--navy);color:#fff;font-size:6.2px;font-weight:700;padding:5px 6px}
.social{top:413px;width:27px;height:27px;border-radius:50%;background:#9a9a9a}
.book-art{left:149px;top:454px;width:99px;height:80px;background:linear-gradient(135deg,#5fb6e6,#1e6fa8 55%,#e8e4dc)}
.book-title{left:258px;top:463px;font-family:"Oswald",sans-serif;font-size:10px}
.book-isbn{left:258px;top:479px;font-size:5px;color:var(--muted)}
.book-text{left:258px;width:330px;font-size:6px;line-height:8px;color:#555}
.program{left:123px;top:539px;width:465px;height:542px;background:var(--panel)}
.item{position:absolute;left:0;width:465px;height:99px}
.item + .item{border-top:1px solid #fff}
.num{position:absolute;left:8px;top:0;width:16px;height:16px;border-radius:50%;background:var(--navy);color:#fff;font-size:9px;font-weight:700;text-align:center;line-height:16px}
.item-title{position:absolute;left:30px;top:2px;font-size:10px;font-weight:700;color:var(--sky)}
.item-icon{position:absolute;left:28px;top:19px;width:49px;height:49px;border:1px solid #ddd;background:#fff;border-radius:3px}
.item-body{position:absolute;left:84px;top:17px;width:375px}
.item-body h4{font-size:7px;color:#222;margin-bottom:2px}
.item-body p{font-size:6.2px;line-height:7.6px;color:#555;font-weight:700;margin-bottom:5px}
.join{left:123px;top:1081px;width:465px;height:21px;border-radius:4px;background:linear-gradient(180deg,#a3d55a,var(--green-dark));color:#fff;font-family:"Oswald",sans-serif;font-size:11px;text-align:center;line-height:21px}
.join:before{content:"";position:absolute;left:225px;top:-6px;border:6px solid transparent;border-top:0;border-bottom-color:#a3d55a}
.footer{left:0;top:1125px;width:711px;border-top:1px solid var(--line)}
.footer-links{left:123px;top:9px;font-size:6.5px;color:#555;white-space:nowrap}
.footer-links span{margin-right:20px}
.copyright{left:123px;top:24px;font-size:6px;color:#666}
</style>
</head>
<body>
<div class="page">
  <header class="site-header abs"><div class="site-name abs">ROWAN ELLERY</div></header>
  <nav class="nav abs">
    <a class="active">Rowan Ellery</a>
    <a style="left:223px">About</a>
    <a style="left:264px">Speaking</a>
    <a style="left:319px">Products</a>
    <a style="left:385px">Programs</a>
    <a style="left:442px">Mentoring</a>
    <a style="left:497px">Testimonials</a>
    <a style="left:558px">Contact</a>
  </nav>
  <section class="hero abs">
    <div class="hero-box abs">
      <div class="portrait abs" role="img" aria-label="Portrait photo of Rowan Ellery"></div>
      <div class="hero-name abs">ROWAN ELLERY</div>
      <ul class="hero-roles abs"><li>Youth Expert</li><li>Motivational Speaker</li><li>Author</li></ul>
      <div class="hero-quote abs">"From a high school dropout to a high school valedictorian, Rowan's goal is to show students how to get back on track"</div>
      <p class="hero-text abs" style="top:45px">Rowan is a youth expert - an author, youth motivational speaker and teen leader who understands the journey of many students today. The former gang member and high school drop out understands the challenges faced by students who are seeking approval and acceptance.</p>
      <p class="hero-text abs" style="top:81px">His journey from gang member to high school teacher was long but gave empowerment and challenges students to make choices, build character and live their best life.</p>
      <div class="read-more abs">Read more ›</div>
    </div>
  </section>

  <h2 class="section-title abs" style="left:123px;top:238px">Video Presentation</h2>
  <div class="video abs">
    <div class="video-frame abs" role="img" aria-label="Video still of Rowan speaking to a seated audience"></div>
    <div class="video-icon abs" style="top:4px"></div>
    <div class="video-icon abs" style="top:22px"></div>
    <div class="video-icon abs" style="top:40px"></div>
    <div class="video-bar abs">
      <svg width="320" height="21" viewBox="0 0 320 21">
        <polygon points="18,6 18,15 26,10.5" fill="#fff"/>
        <rect x="38" y="8" width="16" height="5" fill="#ccc"/>
        <rect x="56" y="9" width="200" height="3" fill="#555"/>
        <rect x="262" y="8" width="26" height="5" fill="#4aa6d8"/>
        <rect x="296" y="6" width="9" height="9" fill="none" stroke="#fff"/>
      </svg>
    </div>
  </div>
  <aside class="optin abs">
    <div class="optin-head abs">Get Rowan's Free ebook on Helping Teens + Updates on Events &amp; Special Offers.</div>
    <label style="top:33px">First Name :</label><div class="field" style="top:43px"></div>
    <label style="top:59px">Email Address :</label><div class="field" style="top:69px"></div>
    <div class="optin-btn abs">Get me the free ebook</div>
    <div class="optin-foot abs">Stay connected with Rowan Ellery</div>
  </aside>
  <div class="social abs" style="left:451px"></div>
  <div class="social abs" style="left:487px"></div>
  <div class="social abs" style="left:523px"></div>
  <div class="social abs" style="left:560px"></div>

  <div class="book-art abs" role="img" aria-label="Book cover and DVD set for Life's Open Road"></div>
  <h3 class="book-title abs">About Book : Life's Open Road</h3>
  <div class="book-isbn abs">ISBN: 000-0-00000-482-3</div>
  <p class="book-text abs" style="top:489px">Life's Open Road: the inspirational story of DJ, a young man struggling with realizing his full potential. After getting into a fight at school, DJ begins to reprioritize his goals and reevaluate where he wants his life to go. He joins a leadership course initially to earn an easy A, but soon forms a bond with a mentor while on a class trip.</p>
  <p class="book-text abs" style="top:519px">In meeting this mentor, DJ learns of ways to improve his life and attitude, giving him a new lease on life.</p>

  <section class="program abs">
    <h2 class="section-title abs" style="left:0;top:22px">What you get when you join the program</h2>
    <div class="item" style="top:54px"><div class="num">1</div><div class="item-title">30 Min. DVD</div><div class="item-icon"></div>
      <div class="item-body"><h4>"Identity" Film</h4><p>The core of the system uses a 15 minute film to engage teens and get their attention. It combines Darren's unique and captivating speaking style with a story that all teens can relate to.</p><h4>A Personal Message</h4><p>This DVD extra is a personal message from Darren on why this issue is so important for them to deal with and how it's changed his life. It's a respectful but firm challenge from Darren to take action and discover their true self.</p></div></div>
    <div class="item" style="top:153px"><div class="num">2</div><div class="item-title">Interactive Q&amp;A Sticker Pack</div><div class="item-icon"></div>
      <div class="item-body"><h4>"Identity" Film</h4><p>The core of the system uses a 15 minute film to engage teens and get their attention. It combines Darren's unique and captivating speaking style with a story that all teens can relate to.</p><h4>A Personal Message</h4><p>This DVD extra is a personal message from Darren on why this issue is so important for them to deal with and how it's changed his life. It's a respectful but firm challenge from Darren to take action and discover their true self.</p></div></div>
    <div class="item" style="top:252px"><div class="num">3</div><div class="item-title">Discover Your Identity Guide Book</div><div class="item-icon"></div>
      <div class="item-body"><h4>"Identity" Film</h4><p>The core of the system uses a 15 minute film to engage teens and get their attention. It combines Darren's unique and captivating speaking style with a story that all teens can relate to.</p><h4>A Personal Message</h4><p>This DVD extra is a personal message from Darren on why this issue is so important for them to deal with and how it's changed his life. It's a respectful but firm challenge from Darren to take action and discover their true self.</p></div></div>
    <div class="item" style="top:351px"><div class="num">4</div><div class="item-title">Resource CD #1</div><div class="item-icon"></div>
      <div class="item-body"><h4>"Identity" Film</h4><p>The core of the system uses a 15 minute film to engage teens and get their attention. It combines Darren's unique and captivating speaking style with a story that all teens can relate to.</p><h4>A Personal Message</h4><p>This DVD extra is a personal message from Darren on why this issue is so important for them to deal with and how it's changed his life. It's a respectful but firm challenge from Darren to take action and discover their true self.</p></div></div>
    <div class="item" style="top:450px"><div class="num">5</div><div class="item-title">Resource CD #2</div><div class="item-icon"></div>
      <div class="item-body"><h4>"Identity" Film</h4><p>The core of the system uses a 15 minute film to engage teens and get their attention. It combines Darren's unique and captivating speaking style with a story that all teens can relate to.</p><h4>A Personal Message</h4><p>This DVD extra is a personal message from Darren on why this issue is so important for them to deal with and how it's changed his life. It's a respectful but firm challenge from Darren to take action and discover their true self.</p></div></div>
  </section>
  <div class="join abs">Join the program</div>

  <footer class="footer abs">
    <div class="footer-links abs"><span>About</span><span>Speaking</span><span>Products</span><span>Programs</span><span>Mentoring</span><span>Testimonials</span><span>Contact</span></div>
    <div class="copyright abs">Copyright © 2012 Rowan Ellery. All Rights Reserved.</div>
  </footer>
</div>
</body>
</html>
```